Banner for Firefighter themed Coffee Company

I need a banner for my home page of my coffee company. It is aimed at Firefighters and first responders in Australia.
I have attached an image i would like incorporated into the banner. Happy for the background to be removed as needed. Maybe incorporate fire and of coffee beans image in background. Or am happy to look at other designs that may suit. Serious with humorous undertones.
Think in the style of Quiet Lantern Coffee Company.
The text reads:
Built for the brave.
Serious coffee for a serious profession.
If possible can I have a web and mobile friendly version.
Target Market(s)
Australian Firefighters and First Responders
Look and feel

```html
<!DOCTYPE html>
<html lang="en">
<head>
<meta charset="utf-8">
<title>Built for the Brave – Banner Sizes</title>
<link rel="stylesheet" href="https://fonts.googleapis.com/css2?family=Bebas+Neue&family=Montserrat:wght@700&family=Oswald:wght@300&family=Poppins:ital,wght@1,300&display=swap">
<style>
  :root{
    --sheet:#ebebeb;
    --ember-dark:#2a0f08;
    --ember-mid:#6b2410;
    --ember-hot:#c4501a;
    --flame:#f08a2a;
    --wood:#6a5140;
    --wood-dark:#4e3a2d;
    --bean:#3b241a;
    --headline:#d6ccb0;
    --gold:#f3b51c;
    --white:#f4f1ea;
    --label:#111111;
    --gear:#c9a227;
  }
  *{margin:0;padding:0;box-sizing:border-box}
  html,body{width:1200px;height:1196px;overflow:hidden;background:var(--sheet)}
  .sheet{position:relative;width:1200px;height:1196px}

  .banner{
    position:absolute;overflow:hidden;
    box-shadow:0 6px 18px rgba(0,0,0,.28);
    background:
      radial-gradient(ellipse 30% 40% at 18% 78%, rgba(240,138,42,.55), transparent 70%),
      radial-gradient(ellipse 35% 45% at 62% 20%, rgba(196,80,26,.55), transparent 70%),
      radial-gradient(ellipse 30% 40% at 95% 10%, rgba(196,80,26,.5), transparent 70%),
      linear-gradient(160deg, var(--ember-mid), var(--ember-dark) 55%, var(--ember-mid));
  }
  .banner--web{left:249px;top:106px;width:702px;height:236px}
  .banner--mobile{left:161px;top:566px;width:878px;height:394px}

  .banner__floor{position:absolute;inset:0;width:100%;height:100%}
  .banner__photo{
    position:absolute;
    background:radial-gradient(ellipse at 50% 55%, rgba(232,190,40,.85), rgba(200,150,30,.55) 45%, transparent 72%);
  }
  .banner--web .banner__photo{left:371px;top:22px;width:292px;height:200px}
  .banner--mobile .banner__photo{left:479px;top:106px;width:376px;height:256px}

  .bean{position:absolute;border-radius:50%;background:var(--bean);transform:rotate(-20deg)}

  .banner__text{position:absolute;z-index:2}
  .headline{
    font-family:"Bebas Neue",sans-serif;color:var(--headline);
    line-height:.85;white-space:nowrap;letter-spacing:.5px;
  }
  .tagline{font-family:"Montserrat",sans-serif;font-weight:700;color:var(--gold);text-transform:uppercase}
  .tagline__light{font-family:"Oswald",sans-serif;font-weight:300;color:var(--white)}

  .banner--web .banner__text{left:24px;top:24px}
  .banner--web .headline{font-size:72px;transform:scaleX(.78);transform-origin:left}
  .banner--web .tagline{font-size:24px;line-height:27px;margin-top:6px;letter-spacing:.3px}

  .banner--mobile .banner__text{left:43px;top:40px}
  .banner--mobile .headline{font-size:132px;transform:scaleX(.86);transform-origin:left}
  .banner--mobile .tagline{font-size:36px;line-height:40px;margin-top:10px;letter-spacing:.5px}

  .size-label{
    position:absolute;left:0;width:1200px;text-align:center;
    font-family:"Poppins",sans-serif;font-style:italic;font-weight:300;
    font-size:66px;color:var(--label);letter-spacing:1px;
  }
  .size-label--web{top:366px}
  .size-label--mobile{top:1002px}
</style>
</head>
<body>
<main class="sheet">

  <section class="banner banner--web" role="img" aria-label="Fire and embers background">
    <svg class="banner__floor" viewBox="0 0 702 236" preserveAspectRatio="none" role="img" aria-label="Wooden floorboards">
      <path d="M0 236 L0 212 C60 200 120 222 190 214 C260 206 290 180 340 176 C380 172 380 150 430 140 C480 130 560 120 620 104 C660 94 690 96 702 96 L702 236 Z" fill="var(--wood)"/>
      <g stroke="var(--wood-dark)" stroke-width="1.5" opacity=".6">
        <line x1="120" y1="236" x2="180" y2="214"/><line x1="260" y1="236" x2="300" y2="190"/>
        <line x1="420" y1="236" x2="430" y2="142"/><line x1="560" y1="236" x2="540" y2="122"/>
        <line x1="660" y1="236" x2="630" y2="104"/>
      </g>
    </svg>
    <div class="banner__photo" role="img" aria-label="Two firefighters in yellow turnout gear riding tricycles joined by a hose"></div>
    <span class="bean" role="img" aria-label="Coffee bean" style="left:530px;top:8px;width:34px;height:20px"></span>
    <span class="bean" role="img" aria-label="Coffee bean" style="left:362px;top:94px;width:30px;height:18px"></span>
    <span class="bean" role="img" aria-label="Coffee bean" style="left:0;top:170px;width:28px;height:18px"></span>
    <span class="bean" role="img" aria-label="Coffee bean" style="left:340px;top:178px;width:26px;height:16px"></span>
    <span class="bean" role="img" aria-label="Coffee bean" style="left:670px;top:200px;width:28px;height:18px"></span>
    <div class="banner__text">
      <h1 class="headline">BUILT FOR THE BRAVE</h1>
      <p class="tagline">Serious Coffee <span class="tagline__light">FOR A</span><br>Serious Profession</p>
    </div>
  </section>
  <p class="size-label size-label--web">1200 x 400 px</p>

  <section class="banner banner--mobile" role="img" aria-label="Fire and embers background">
    <svg class="banner__floor" viewBox="0 0 878 394" preserveAspectRatio="none" role="img" aria-label="Wooden floorboards">
      <path d="M0 394 L0 340 C60 320 140 346 220 332 C320 316 380 300 440 276 C500 250 520 220 580 206 C640 192 700 196 760 186 C820 176 860 168 878 166 L878 394 Z" fill="var(--wood)"/>
      <g stroke="var(--wood-dark)" stroke-width="2" opacity=".6">
        <line x1="150" y1="394" x2="230" y2="330"/><line x1="330" y1="394" x2="380" y2="302"/>
        <line x1="520" y1="394" x2="540" y2="220"/><line x1="700" y1="394" x2="680" y2="196"/>
        <line x1="820" y1="394" x2="790" y2="180"/>
      </g>
    </svg>
    <div class="banner__photo" role="img" aria-label="Two firefighters in yellow turnout gear riding tricycles joined by a hose"></div>
    <span class="bean" role="img" aria-label="Coffee bean" style="left:720px;top:4px;width:62px;height:40px"></span>
    <span class="bean" role="img" aria-label="Coffee bean" style="left:328px;top:204px;width:42px;height:26px"></span>
    <span class="bean" role="img" aria-label="Coffee bean" style="left:376px;top:226px;width:34px;height:22px"></span>
    <span class="bean" role="img" aria-label="Coffee bean" style="left:6px;top:262px;width:46px;height:30px"></span>
    <span class="bean" role="img" aria-label="Coffee bean" style="left:400px;top:310px;width:40px;height:26px"></span>
    <span class="bean" role="img" aria-label="Coffee bean" style="left:876px;top:190px;width:30px;height:20px"></span>
    <div class="banner__text">
      <h2 class="headline">BUILT FOR THE BRAVE</h2>
      <p class="tagline">Serious Coffee <span class="tagline__light">FOR A</span><br>Serious<br>Profession</p>
    </div>
  </section>
  <p class="size-label size-label--mobile">2400 x 1080 px</p>

</main>
</body>
</html>
```